Small Machinery Hire Company Needs Coaster Design

Please design an eye catching coaster/sticker to place in local pubs and restaurants. Please use our attached logo and incorporate our rustic earthy feel into the colours. Use the following details. Definite want the focus to be on the logo and phone number.

Would appreciate if it could be multi-purpose as a basic sign as well.

Dry/Wet Hire Available
Ph: 0471629058

(Use FaceBook icon) facebook.com/bramwellkestrelplant2917/

Target Market(s)

At homer DIY-ers. Middle class men who would like to hire a machine to work on their own pride and joy home.

Industry/Entity Type

Construction Company

Font styles to use
Other font styles liked:
• Something that matches the Logo

Colors
fefdec
ec1f27
474747
919191

Requirements
Nice to have
• Preferably a square shape so the it is more multi purpose

```html
<!DOCTYPE html>
<html lang="en">
<head>
<meta charset="utf-8">
<title>Bramwell Kestrel Plant – Coaster</title>
<link href="https://fonts.googleapis.com/css2?family=Rye&family=Roboto+Slab:wght@800&family=Montserrat:ital,wght@1,700&display=swap" rel="stylesheet">
<style>
  :root {
    --backdrop: #1c1c1c;
    --wood-light: #d9bf92;
    --wood-mid: #c4a26d;
    --wood-dark: #9c7b4c;
    --ink: #1b1712;
    --brand-red: #8a1212;
    --band: #0d0d0d;
    --band-text: #ffffff;
  }
  html, body {
    margin: 0;
    width: 1200px;
    height: 1200px;
    overflow: hidden;
    background: var(--backdrop);
  }
  .coaster {
    position: absolute;
    left: 100px;
    top: 100px;
    width: 1000px;
    height: 1000px;
  }
  .tagline {
    font-family: "Rye", serif;
    font-size: 62px;
    fill: var(--ink);
    letter-spacing: 3px;
  }
  .brand-name {
    font-family: "Rye", serif;
    fill: var(--brand-red);
    text-anchor: middle;
  }
  .brand-name--top { font-size: 150px; }
  .brand-name--bottom { font-size: 92px; }
  .phone-number {
    font-family: "Roboto Slab", serif;
    font-weight: 800;
    font-size: 58px;
    fill: var(--band-text);
  }
  .social-handle {
    font-family: "Montserrat", sans-serif;
    font-style: italic;
    font-weight: 700;
    font-size: 36px;
    fill: var(--ink);
  }
</style>
</head>
<body>
<svg class="coaster" viewBox="0 0 1000 1000" xmlns="http://www.w3.org/2000/svg">
  <defs>
    <linearGradient id="wood-tone" x1="0" y1="0" x2="1" y2="1">
      <stop offset="0" stop-color="var(--wood-mid)"/>
      <stop offset="0.45" stop-color="var(--wood-light)"/>
      <stop offset="1" stop-color="var(--wood-dark)"/>
    </linearGradient>
    <path id="tagline-arc" d="M110 330 A 400 330 0 0 1 890 330"/>
  </defs>

  <rect class="coaster-surface" role="img" aria-label="Weathered light timber grain surface"
        x="0" y="0" width="1000" height="1000" rx="44" fill="url(#wood-tone)"/>

  <text class="tagline"><textPath href="#tagline-arc" startOffset="50%" text-anchor="middle">DRY/WET HIRE AVAILABLE</textPath></text>

  <text class="brand-name brand-name--top" x="500" y="480" textLength="820" lengthAdjust="spacingAndGlyphs">BRAMWELL</text>
  <text class="brand-name brand-name--bottom" x="500" y="600" textLength="780" lengthAdjust="spacingAndGlyphs">KESTREL PLANT</text>

  <g class="phone-band">
    <rect x="220" y="650" width="560" height="100" fill="var(--band)"/>
    <path class="phone-icon" transform="translate(284 678) scale(1.8)" fill="var(--band-text)"
          d="M6.62 10.79c1.44 2.83 3.76 5.14 6.59 6.59l2.2-2.2c.27-.27.67-.36 1.02-.24 1.12.37 2.33.57 3.57.57.55 0 1 .45 1 1V20c0 .55-.45 1-1 1-9.39 0-17-7.61-17-17 0-.55.45-1 1-1h3.5c.55 0 1 .45 1 1 0 1.25.2 2.45.57 3.57.11.35.03.74-.25 1.02l-2.2 2.2z"/>
    <text class="phone-number" x="350" y="720" textLength="370" lengthAdjust="spacingAndGlyphs">0471 629 058</text>
  </g>

  <g class="social-line">
    <rect x="210" y="808" width="40" height="40" rx="6" fill="var(--ink)"/>
    <text class="social-handle" x="263" y="840" textLength="540" lengthAdjust="spacingAndGlyphs">bramwellkestrelplant2917</text>
  </g>
</svg>
</body>
</html>
```